Quillmont Billboard - Financial Services Company (Investments, Tax Planning and Insurance)

Our new office has a billboard directly above the office building. We'd like something eye-catching with a strong Call to Action, with the main part of the billboard being under 7 words if possible. We'd like you to include a way to get ahold of us (either our website quillmontllc.example or our phone number 302-418-2267. You may also include in small font something to indicate that we've been serving the area since 1980 (the DE area, the tri-state area, the Ashgrove Hollow, etc.)

We offer financial planning, tax planning, and insurance, and we help our clients to focus on their goals and happiness by providing everything they need for lifelong wealth under one roof.

Our logos are attached, we use a triangle logo with green and gray. We use the tagline "experience lifelong wealth" but this does not need to be included.

Potential ideas we have seen from other financial companies-
- the concept that the driver spends more time looking at billboards than planning for their retirement
-something along the lines of "everything you need for your finances is in this building right here" planning, investments, taxes, insurance"
-don't spend your time worrying about retirement, let us help you plan for it
-are you working for your money, or is it working for you?
- retirement takes planning, we're here to help
- ready to retire? talk to us
- need investment advice?
- need help investing?
- crossing your fingers isn't a retirement plan. we can help.
- retiring soon? you need help.

Those are just general ideas, please feel free to be creative.

brand colors:
#00b585
#00b185
#000000
#ffffff
#6d6f75
#6d6f75
#6f7074
#021712
#052e24

```html
<!DOCTYPE html>
<html lang="en">
<head>
<meta charset="utf-8">
<title>Quillmont Billboard</title>
<link rel="stylesheet" href="https://fonts.googleapis.com/css2?family=Anton&family=Libre+Baskerville:wght@700&family=Montserrat:wght@700&display=swap">
<style>
  :root {
    --forest-deep: #02380a;
    --forest: #0d5a15;
    --leaf: #2a8a2a;
    --lime: #8fff70;
    --brand-green: #2bd63a;
    --divider-green: #1f8a1f;
    --slate: #56636b;
    --mist: #e1e7e5;
    --sun: #f9ec12;
    --white: #ffffff;
    --footer: #02350a;
  }
  * { margin: 0; padding: 0; box-sizing: border-box; }
  html, body { width: 1200px; height: 599px; overflow: hidden; background: var(--white); }
  .billboard { position: relative; width: 1200px; height: 599px; overflow: hidden; background: var(--white); }
  .billboard__backdrop { position: absolute; inset: 0; }

  .headline {
    position: absolute; left: 58px; top: 31px;
    font-family: "Anton", "Oswald", sans-serif; font-weight: 400;
    font-size: 110px; line-height: 126px;
    color: var(--white); text-transform: uppercase;
    letter-spacing: 1px;
  }
  .headline__line {
    display: block; white-space: nowrap;
    transform: scaleX(1.23); transform-origin: left center;
  }
  .headline__answer { color: var(--sun); margin-left: 12px; }

  .brand {
    position: absolute; left: 832px; top: 30px; height: 60px;
    display: flex; align-items: center; gap: 16px;
  }
  .brand__dot { width: 56px; height: 56px; border-radius: 50%; background: var(--brand-green); flex: none; }
  .brand__name {
    font-family: "Montserrat", Arial, sans-serif; font-weight: 700;
    font-size: 46px; line-height: 1; color: var(--brand-green);
    letter-spacing: -0.5px;
  }

  .services {
    position: absolute; left: 0; top: 417px; width: 1200px; height: 95px;
    background: linear-gradient(90deg, var(--mist) 0%, #f4f6f5 60%, var(--white) 100%);
    display: flex; align-items: center; justify-content: center; gap: 24px;
    font-family: "Libre Baskerville", Georgia, serif; font-weight: 700;
    font-size: 47px; color: var(--slate);
    padding-bottom: 6px;
  }
  .services__divider { width: 3px; height: 42px; background: var(--divider-green); }

  .contact {
    position: absolute; left: 0; top: 512px; width: 1200px; height: 87px;
    background: var(--footer);
    display: flex; align-items: center; padding-left: 54px;
    font-family: "Montserrat", Arial, sans-serif; font-weight: 700;
    color: var(--white);
  }
  .contact__icon { width: 52px; height: 52px; flex: none; }
  .contact__phone { font-size: 58px; letter-spacing: -1.5px; margin-left: 12px; }
  .contact__divider { width: 3px; height: 42px; background: var(--white); margin: 0 24px 0 24px; }
  .contact__web { font-size: 44px; margin-left: 12px; letter-spacing: -0.5px; }
</style>
</head>
<body>
<main class="billboard">
  <svg class="billboard__backdrop" width="1200" height="599" viewBox="0 0 1200 599" aria-hidden="true">
    <defs>
      <linearGradient id="bannerFade" x1="0" y1="0" x2="1" y2="0">
        <stop offset="0" stop-color="#02380a"/>
        <stop offset="0.3" stop-color="#0d5a15"/>
        <stop offset="0.58" stop-color="#2a8a2a"/>
        <stop offset="0.72" stop-color="#4fbf46"/>
        <stop offset="0.85" stop-color="#8fff70"/>
        <stop offset="1" stop-color="#8fff70"/>
      </linearGradient>
    </defs>
    <polygon points="0,12 762,12 809,124 1200,124 1200,417 0,417" fill="url(#bannerFade)"/>
  </svg>

  <div class="brand">
    <span class="brand__dot"></span>
    <span class="brand__name">Quillmont</span>
  </div>

  <h1 class="headline">
    <span class="headline__line">Worrying</span>
    <span class="headline__line">About Your</span>
    <span class="headline__line">Money?<span class="headline__answer">Us Too!</span></span>
  </h1>

  <div class="services">
    <span>Planning</span><span class="services__divider"></span>
    <span>Investments</span><span class="services__divider"></span>
    <span>Taxes</span><span class="services__divider"></span>
    <span>Insurance</span>
  </div>

  <div class="contact">
    <svg class="contact__icon" viewBox="0 0 52 52" aria-hidden="true">
      <circle cx="26" cy="26" r="26" fill="#fff"/>
      <path d="M17 14c2-1 3 0 4 2l2 4c1 2 0 3-1 4l-1 1c1 3 4 6 7 7l1-1c1-1 2-2 4-1l4 2c2 1 3 2 2 4l-1 2c-1 2-3 3-6 2-8-2-14-8-16-16-1-3 0-5 2-6z" fill="#02350a"/>
      <path d="M29 14a10 10 0 0 1 9 9M29 19a5 5 0 0 1 4 4" stroke="#02350a" stroke-width="2.5" fill="none" stroke-linecap="round"/>
    </svg>
    <span class="contact__phone">302-418-2267</span>
    <span class="contact__divider"></span>
    <svg class="contact__icon" viewBox="0 0 52 52" aria-hidden="true">
      <circle cx="26" cy="26" r="26" fill="#fff"/>
      <g stroke="#02350a" stroke-width="2.2" fill="none">
        <circle cx="26" cy="26" r="15"/>
        <ellipse cx="26" cy="26" rx="7" ry="15"/>
        <line x1="26" y1="11" x2="26" y2="41"/>
        <line x1="11" y1="26" x2="41" y2="26"/>
        <path d="M14 18h24M14 34h24"/>
      </g>
    </svg>
    <span class="contact__web">quillmontllc.example</span>
  </div>
</main>
</body>
</html>
```